Letterhead/Envelope Design Project

We are a 501c3 non-profit that supports educational programs at Dunmoral Fern Hollow State Park in California. We have new logo and need letterhead. The design needs need incorporate the logo attached. It needs to contain the information in document attached called "information" attached. Please see our website fernhollow.org to get the feeling and colors we are looking for.

```html
<!DOCTYPE html>
<html lang="en">
<head>
<meta charset="utf-8">
<title>Dunmoral Fern Hollow Association Letterhead</title>
<link rel="stylesheet" href="https://fonts.googleapis.com/css2?family=PT+Sans:wght@400&display=swap">
<style>
  :root {
    --forest: #1c4b1d;
    --forest-deep: #073507;
    --gold: #e9b71a;
    --paper: #ffffff;
    --mark-square: #3f7a3a;
  }
  * { margin: 0; padding: 0; box-sizing: border-box; }
  html, body { width: 927px; height: 1200px; overflow: hidden; background: var(--paper); }
  body { font-family: "PT Sans", sans-serif; }
  .letterhead { position: relative; width: 927px; height: 1200px; background: var(--paper); }

  .masthead { position: absolute; left: 0; top: 0; width: 927px; height: 107px; background: var(--forest); }
  .tagline-band { position: absolute; left: 0; top: 107px; width: 927px; height: 29px; background: var(--forest-deep); }
  .tagline {
    position: absolute; left: 182px; top: 5px;
    color: var(--gold); font-size: 17px; letter-spacing: 4.6px; line-height: 19px;
    text-transform: uppercase;
  }

  .brand {
    position: absolute; left: 67px; top: 24px; height: 60px;
    display: flex; align-items: center; gap: 14px;
  }
  .brand-square { width: 60px; height: 60px; background: var(--mark-square); flex: none; }
  .brand-name {
    color: var(--gold); font-weight: 400;
    font-size: 16px; line-height: 19px;
  }

  .contact {
    position: absolute; left: 751px; top: 23px;
    color: var(--gold); font-size: 8.2px; line-height: 11.2px; list-style: none;
  }

  .mission-band {
    position: absolute; left: 0; bottom: 0; width: 927px; height: 37px; background: var(--forest-deep);
    display: flex; align-items: center; justify-content: center;
  }
  .mission { color: var(--gold); font-size: 14.2px; white-space: nowrap; }
</style>
</head>
<body>
<div class="letterhead">
  <header class="masthead">
    <div class="brand">
      <div class="brand-square"></div>
      <p class="brand-name">Dunmoral Fern Hollow<br>Association</p>
    </div>
    <ul class="contact">
      <li>Dunmoral Fern Hollow Association</li>
      <li>P.O. Box 4820</li>
      <li>Larkfield, CA 95402-4820</li>
      <li>Phone: 209.555.0148</li>
      <li>Fax: 209.555.0162</li>
      <li>email: info@fernhollow.org</li>
      <li>website: fernhollow.org</li>
    </ul>
  </header>
  <div class="tagline-band">
    <p class="tagline">Walking in awe among giants</p>
  </div>
  <footer class="mission-band">
    <p class="mission">Our Mission: To support the delivery of high quality educational and interpretive programs at Dunmoral Fern Hollow State Park</p>
  </footer>
</div>
</body>
</html>
```